Tova Brisk Fitness Coaching Project

I am a personal trainer based in London. My services include one-on-one PT sessions, bootcamps.
I would like the design to be minimalistic. With light colours: white, pink, purple.
I specialise in weight loss, flexibility, mobility.

Tova Penrick
Personal Trainer
Email: tova.penrick@mailgrove.net
tel: 07500 918 243
Instagram: Tova Brisk

Target Market(s)

adults, mostly females (age 18-50).

Industry/Entity Type

Fitness

Contact Information for Business Card

Tova Penrick
Personal Trainer
tel: 07500 918 243
Instagram: Tova Brisk

Font styles to use
Serif

Colors
eea4c8
fbd4d5
fdf9cf
cfeae6
cee9f5

Requirements
Nice to have
• minimalistic style
• easy to read and remember

```html
<!DOCTYPE html>
<html lang="en">
<head>
<meta charset="utf-8">
<title>Tova Penrick – Personal Trainer Business Card</title>
<link rel="stylesheet" href="https://fonts.googleapis.com/css2?family=Cabin:wght@400&display=swap">
<style>
  :root {
    --page: #ffffff;
    --ink: #1e1d22;
    --navy: #262c55;
    --slate: #8e97a8;
    --slate-deep: #5f6b86;
    --teal: #8fcfc3;
    --purple: #a06a9e;
    --pink: #e49bbd;
    --cream: #e6dfc4;
    --sand: #cfc2a6;
  }
  * { margin: 0; padding: 0; box-sizing: border-box; }
  html, body {
    width: 1200px;
    height: 1200px;
    overflow: hidden;
    background: var(--page);
  }
  .business-card {
    position: absolute;
    left: 100px;
    top: 315px;
    width: 1000px;
    height: 570px;
    overflow: hidden;
    font-family: "Cabin", sans-serif;
    color: var(--ink);
  }
  .card-photo {
    position: absolute;
    inset: 0;
    background:
      radial-gradient(ellipse 18% 26% at 33% 40%, rgba(143, 207, 195, 0.9), transparent 70%),
      radial-gradient(ellipse 22% 30% at 60% 45%, rgba(228, 155, 189, 0.7), transparent 70%),
      linear-gradient(100deg, #9aa1ac 0%, #7d8593 22%, #b7a49a 45%, #c9a8a6 65%, #bfae92 100%);
  }
  .card-overlay {
    position: absolute;
    inset: 0;
    width: 100%;
    height: 100%;
  }
  .card-name,
  .card-title {
    position: absolute;
    left: 580px;
    width: 450px;
    text-align: center;
    font-size: 41px;
    line-height: 1;
    letter-spacing: -0.2px;
  }
  .card-name { top: 262px; left: 553px; width: 500px; }
  .card-title { top: 322px; left: 550px; width: 500px; }
  .card-contact {
    position: absolute;
    left: 602px;
    top: 420px;
    list-style: none;
    font-size: 23px;
    line-height: 36px;
  }
</style>
</head>
<body>
  <div class="business-card">
    <div class="card-photo" role="img" aria-label="Photograph of women doing squats with arms stretched forward in a fitness class"></div>
    <svg class="card-overlay" viewBox="0 0 585 333" preserveAspectRatio="none" aria-hidden="true">
      <polygon points="0,0 165,0 230,140 175,333 0,333" fill="var(--slate)" opacity="0.45"/>
      <polygon points="170,0 585,0 585,90 370,112 290,205 235,130" fill="var(--purple)" opacity="0.55"/>
      <polygon points="370,112 585,90 585,333 285,333 345,215 330,160" fill="var(--cream)" opacity="0.6"/>
      <polygon points="0,260 0,333 55,333" fill="var(--slate-deep)" opacity="0.55"/>
      <g fill="none" stroke="var(--navy)" stroke-width="6" stroke-linejoin="miter">
        <polyline points="160,0 222,130"/>
        <polyline points="585,90 372,110 292,205"/>
        <polyline points="338,200 280,333"/>
        <polyline points="0,268 70,333"/>
      </g>
      <g fill="none" stroke="var(--sand)" stroke-width="3" opacity="0.7">
        <polyline points="300,333 362,220 420,333"/>
      </g>
    </svg>
    <p class="card-name">Tova Penrick</p>
    <p class="card-title">Personal Trainer</p>
    <ul class="card-contact">
      <li>Email: tova.penrick@mailgrove.net</li>
      <li>tel: 07500 918 243</li>
      <li>Instagram: Tova Brisk</li>
    </ul>
  </div>
</body>
</html>
```